law firm website

We need a website for our law firm that is based in Kabul, Afghanistan. We provide legal and government affairs services for the international community. We would like to see designs that use the colors of our logo, designs that are elegant and simple, yet not boring or over the top. No law or law related symbols or pictures. We would like clocks that show times for Kabul, Dubai and Washington DC.
Updates
Reason: No designs that are up to the task as yet. Perhaps we should stop using picture of people, that obviously don't work with us, in the website. If you are to use pictures, please try using pictures of Afghanistan mountains, art, craft etc. Also, please make the clocks very small - they seem to be dominating the website. We do not sell clocks or watches - we are a law firm. Hope you all understand and thank you for your designs to date.
Deal All,
Industry/Entity Type
Government
Requirements
Must have
- our logo.
the following phrases/words in flash.
"international standards" "local expertise" "integrity" "clarity" "commitment" "Afghanistan"
clocks: kabul, dubai, washington dc
Should not have
- law related pictures
afghanistan flag colors

```html
<!DOCTYPE html>
<html lang="en">
<head>
<meta charset="utf-8">
<title>Hindukush Legal Partners</title>
<link href="https://fonts.googleapis.com/css2?family=Open+Sans:wght@400;600;700&family=Roboto:wght@400;500&family=Roboto+Condensed:wght@400;700&display=swap" rel="stylesheet">
<style>
:root{
  --blue:#2ea3d8;
  --blue-dark:#1d8fc4;
  --band:#0d9ad6;
  --ink:#333;
  --text:#444;
  --muted:#777;
  --nav:#2b2b2b;
  --page:#f4f4f4;
  --grey-sec:#efefef;
  --footer:#333;
  --white:#fff;
}
*{box-sizing:border-box;margin:0;padding:0}
html,body{width:1075px;height:1200px;overflow:hidden}
body{position:relative;background:var(--white);font-family:"Open Sans",sans-serif;color:var(--text)}
.top{position:absolute;left:0;top:0;width:1075px;height:137px;background:var(--page);border-bottom:1px solid #ddd}
.map-bg{position:absolute;left:0;top:230px;width:1075px;height:420px;background:radial-gradient(ellipse at 15% 35%,rgba(175,215,235,.45),transparent 30%),radial-gradient(ellipse at 48% 70%,rgba(175,215,235,.45),transparent 28%),radial-gradient(ellipse at 92% 45%,rgba(175,215,235,.45),transparent 22%)}
.brand{position:absolute;left:128px;top:40px;display:flex;align-items:center;gap:10px;font-size:17px;color:#5a8fb0}
.brand .mark{width:14px;height:14px;background:#333}
.clock{position:absolute;top:8px;text-align:center;font-family:"Roboto",serif;font-size:13px;letter-spacing:1px;color:#222}
.clock svg{display:block;margin:0 auto 2px}
.nav{position:absolute;left:126px;top:116px;width:823px;height:42px;background:repeating-linear-gradient(135deg,#2f2f2f 0 2px,#282828 2px 4px);border-radius:3px;display:flex;align-items:center;padding-left:26px;font-family:"Roboto",sans-serif;font-size:14px}
.nav a{color:#fff;text-decoration:none;margin-right:34px}
.nav a.active{color:var(--blue)}
.nav .lexnet{background:#fff;color:var(--blue);font-weight:500;padding:7px 14px;border-radius:2px;margin-right:16px}
.search{width:173px;height:28px;background:#555;border-radius:2px;color:#aaa;font-size:11px;padding:7px 8px;position:relative}
.search svg{position:absolute;right:6px;top:7px}
.hero{position:absolute;left:126px;top:175px;width:823px;height:336px;border:1px solid #ccc;background:#fff;padding:4px}
.hero-img{width:100%;height:100%;background:linear-gradient(100deg,#2b2b2b 0%,#6f7a80 35%,#c7a593 55%,#8fa0a8 75%,#2e3438 100%)}
.caption{position:absolute;left:297px;top:72px;width:493px;height:146px;background:rgba(245,245,245,.93);padding:10px 18px}
.caption h2{font-family:"Roboto Condensed",sans-serif;font-weight:700;color:var(--blue);font-size:36px;line-height:40px}
.caption p{font-family:"Roboto Condensed",sans-serif;color:#333;font-size:21px;line-height:25px;margin-top:6px}
.dots{position:absolute;right:16px;bottom:14px;display:flex;gap:7px}
.dots span{width:12px;height:12px;border-radius:50%;background:#ddd}
.dots span.on{background:var(--blue)}
.welcome{position:absolute;left:128px;top:533px;width:529px}
.welcome small{font-family:"Roboto",sans-serif;font-size:17px;color:#222}
.welcome h1{font-family:"Roboto",sans-serif;font-weight:400;color:var(--blue);font-size:27px;line-height:30px;padding-bottom:8px;border-bottom:1px dashed #ccc;margin-bottom:8px}
.welcome p{font-size:11px;line-height:19.7px;margin-bottom:8px;text-align:justify}
.more{display:inline-block;font-size:11px;font-weight:700;color:#222}
.more-btn{position:absolute;left:126px;top:781px;background:#eee;padding:5px 10px}
.services{position:absolute;left:697px;top:527px;width:252px;height:277px;background:var(--blue);border:2px solid #fff;box-shadow:0 2px 6px rgba(0,0,0,.2)}
.services .tab{position:absolute;left:44px;top:-4px;width:138px;height:44px;background:#fff;box-shadow:0 2px 4px rgba(0,0,0,.2);font-family:"Roboto",sans-serif;font-size:21px;color:#111;text-align:center;line-height:46px}
.services .lead{position:absolute;top:57px;left:8px;right:8px;color:#fff;font-weight:700;font-size:12.5px;line-height:18px}
.services ul{position:absolute;top:101px;left:0;right:0;list-style:none}
.services li{height:34px;border-top:1px solid rgba(255,255,255,.35);color:#fff;font-size:15.5px;line-height:33px;padding-left:9px;position:relative}
.services li.on{background:#333}
.services li.on svg{position:absolute;right:10px;top:10px}
.services .more{position:absolute;right:10px;bottom:10px;color:#111}
.grey{position:absolute;left:0;top:822px;width:1075px;height:161px;background:var(--grey-sec);border-top:1px solid #ddd}
.sec-title{position:absolute;font-family:"Roboto",sans-serif;font-size:19px;color:#222;display:flex;align-items:center;gap:8px;border-bottom:1px dashed #ccc;padding-bottom:8px}
.sec-title b{font-weight:400;color:var(--blue)}
.quote{position:absolute;top:890px;width:270px;display:flex;gap:8px}
.avatar{width:64px;height:67px;border:1px solid #ccc;background:#fff;padding:3px;flex:none}
.avatar div{width:100%;height:100%;background:linear-gradient(#e9ecee,#b9c1c7)}
.quote p{font-size:11.5px;line-height:16px;color:#333}
.quote p strong{color:#222}
.quote .by{color:var(--blue);font-weight:600;font-size:11px;margin-top:6px}
.ethics-text{position:absolute;left:696px;top:888px;width:253px;display:flex;gap:8px;font-size:11.5px;font-weight:700;color:#333;line-height:15.5px}
.ethics-more{position:absolute;left:906px;top:938px}
.arrows{position:absolute;left:913px;top:845px;display:flex;gap:4px}
.arrows span{width:15px;height:15px;border-radius:50%;border:1px solid #bbb;background:#fff}
.news{position:absolute;left:0;top:983px;width:1075px;height:43px;background:var(--band);display:flex;align-items:center;padding-left:128px}
.news h3{color:#fff;font-size:16.5px;font-weight:600;margin-right:16px}
.news .email{width:192px;height:28px;background:#fff;font-size:10.5px;font-style:italic;color:#999;padding:6px 8px;margin-right:8px}
.news .sub{background:#111;color:#fff;font-family:"Roboto",sans-serif;font-weight:500;font-size:12.5px;padding:6px 10px}
.social{position:absolute;right:128px;top:10px;display:flex;gap:4px}
.social span{width:23px;height:23px;border-radius:50%;border:2px solid #fff;background:#1a6fa8}
.footer{position:absolute;left:0;top:1026px;width:1075px;height:174px;background:var(--footer);color:#ddd;font-size:11px}
.footer h4{position:absolute;font-family:"Roboto",sans-serif;font-weight:400;font-size:17.5px;color:#fff;border-bottom:1px solid #888;padding-bottom:6px}
.links{position:absolute;top:54px;list-style:none;line-height:21px}
.links li::before{content:"›";margin-right:5px}
.office{position:absolute;top:54px;width:205px;line-height:17px}
.office b{color:#fff;font-size:12px;display:block;margin-bottom:4px}
.row{display:flex;gap:8px;margin-bottom:5px}
.row svg{flex:none;margin-top:2px}
.vrule{position:absolute;top:20px;width:1px;height:145px;background:#444}
.copy{position:absolute;left:746px;top:86px;width:216px;text-align:center;line-height:16px}
.copy .name{font-size:15px;color:#777;margin-bottom:6px}
</style>
</head>
<body>
<div class="top"></div>
<div class="map-bg" role="img" aria-label="Faint world map in light blue behind the page"></div>

<header>
  <div class="brand"><span class="mark"></span>Hindukush Legal Partners</div>
  <div class="clock" style="left:608px;width:70px">
    <svg width="68" height="68" viewBox="0 0 68 68"><circle cx="34" cy="34" r="31" fill="#fff" stroke="#39a5d6" stroke-width="4"/><g stroke="#555" stroke-width="1.5"><line x1="34" y1="7" x2="34" y2="12"/><line x1="34" y1="56" x2="34" y2="61"/><line x1="7" y1="34" x2="12" y2="34"/><line x1="56" y1="34" x2="61" y2="34"/></g><line x1="34" y1="34" x2="34" y2="17" stroke="#111" stroke-width="2"/><line x1="34" y1="34" x2="46" y2="40" stroke="#111" stroke-width="2"/></svg>KABUL</div>
  <div class="clock" style="left:725px;width:70px">
    <svg width="68" height="68" viewBox="0 0 68 68"><circle cx="34" cy="34" r="31" fill="#fff" stroke="#39a5d6" stroke-width="4"/><g stroke="#555" stroke-width="1.5"><line x1="34" y1="7" x2="34" y2="12"/><line x1="34" y1="56" x2="34" y2="61"/><line x1="7" y1="34" x2="12" y2="34"/><line x1="56" y1="34" x2="61" y2="34"/></g><line x1="34" y1="34" x2="26" y2="20" stroke="#111" stroke-width="2"/><line x1="34" y1="34" x2="48" y2="42" stroke="#111" stroke-width="2"/></svg>DUBAI</div>
  <div class="clock" style="left:822px;width:130px">
    <svg width="68" height="68" viewBox="0 0 68 68"><circle cx="34" cy="34" r="31" fill="#fff" stroke="#39a5d6" stroke-width="4"/><g stroke="#555" stroke-width="1.5"><line x1="34" y1="7" x2="34" y2="12"/><line x1="34" y1="56" x2="34" y2="61"/><line x1="7" y1="34" x2="12" y2="34"/><line x1="56" y1="34" x2="61" y2="34"/></g><line x1="34" y1="34" x2="46" y2="24" stroke="#111" stroke-width="2"/><line x1="34" y1="34" x2="20" y2="46" stroke="#111" stroke-width="2"/></svg>WASHINGTON DC</div>
</header>

<nav class="nav">
  <a class="active" href="#">About</a><a href="#">People</a><a href="#">Services</a><a href="#">Ethics</a><a href="#">Publications</a><a href="#">Contact</a>
  <a class="lexnet" href="#">LexNet</a>
  <div class="search">Search<svg width="13" height="13" viewBox="0 0 13 13"><circle cx="5.5" cy="5.5" r="4.3" fill="none" stroke="#111" stroke-width="1.8"/><line x1="8.6" y1="8.6" x2="12" y2="12" stroke="#111" stroke-width="2"/></svg></div>
</nav>

<section class="hero">
  <div class="hero-img" role="img" aria-label="Photograph of two people in suits shaking hands"></div>
  <div class="caption">
    <h2>INTERNATIONAL STANDARDS</h2>
    <p>Lorem ipsum dolor sit amet, consectetue adipiscing elit, sed diam nonummy nibh euismod tincidunt ut laoreet dolore magna aliquam erat volutpat.</p>
  </div>
  <div class="dots"><span class="on"></span><span></span><span></span><span></span></div>
</section>

<section class="welcome">
  <small>Welcome to</small>
  <h1>Hindukush Legal Partners</h1>
  <p>Hindukush Legal Partners (HLP) is an Afghan legal and government affairs advisory firm staffed by a number of highly experienced lawyers and advisors qualified in Afghanistan, the United States and Australia.</p>
  <p>The two principals of HLP have over a decade of legal and government affairs advisory experience in Afghanistan advising investors, local and foreign government agencies and non-governmental organisations on some of the largest and most complex matters, transactions, projects and financings across several sectors including mining and infrastructure, telecommunications, oil &amp; gas, construction, media, aviation and banking and financial services.</p>
</section>
<a class="more more-btn" href="#">More »</a>

<aside class="services">
  <div class="tab">SERVICES</div>
  <p class="lead">We provide exceptional, practical and cost-effective services</p>
  <ul>
    <li>Corporate and investment</li>
    <li class="on">Projects<svg width="16" height="14" viewBox="0 0 16 14"><path d="M2 1l6 6-6 6M8 1l6 6-6 6" fill="none" stroke="#ccc" stroke-width="1.6"/></svg></li>
    <li>Commercial contracts</li>
    <li>Financings</li>
  </ul>
  <span class="more">More »</span>
</aside>

<section class="grey"></section>
<div class="sec-title" style="left:126px;top:840px;width:531px">
  <svg width="20" height="18" viewBox="0 0 20 18"><path d="M1 1h11v8H6l-3 3V9H1z" fill="#2ea3d8"/><path d="M14 5h5v8h-2v3l-3-3H8v-2h6z" fill="#2ea3d8"/></svg>Our <b>Client Says</b></div>
<div class="quote" style="left:126px">
  <div class="avatar"><div role="img" aria-label="Portrait photo of a client"></div></div>
  <div><p><strong>Lorem ipsum dolor sit amet,</strong> sed diam nonummy nibh euismod tincidunt ut laor dolore magna</p><p class="by">- Lorem ipsum dolor</p></div>
</div>
<div class="quote" style="left:407px">
  <div class="avatar"><div role="img" aria-label="Portrait photo of a client"></div></div>
  <div><p><strong>Lorem ipsum dolor sit amet,</strong> sed diam nonummy nibh euismod tincidunt ut laor dolore magna</p><p class="by">- Lorem ipsum dolor</p></div>
</div>
<div class="sec-title" style="left:696px;top:840px;width:253px">
  <svg width="14" height="18" viewBox="0 0 14 18"><rect x="1" y="1" width="12" height="16" fill="none" stroke="#2ea3d8" stroke-width="1.8"/><path d="M3 12l3-4 2 2 3-4" fill="none" stroke="#2ea3d8" stroke-width="1.5"/></svg>Ethics</div>
<div class="arrows"><span></span><span></span></div>
<div class="ethics-text"><svg width="14" height="14" viewBox="0 0 14 14" style="flex:none"><circle cx="7" cy="7" r="6" fill="none" stroke="#2ea3d8" stroke-width="1.4"/><path d="M4 7l2 2 5-6" fill="none" stroke="#2ea3d8" stroke-width="1.8"/></svg>Maintain the highest standards of integrity, fairness, honesty and respect in all our dealings.</div>
<span class="more ethics-more">More »</span>

<section class="news">
  <h3>Keep up to date with our latest news.</h3>
  <div class="email">Enter your email here</div>
  <div class="sub">SUBSCRIBE</div>
  <div class="social"><span></span><span style="background:#b3273b"></span><span style="background:#2a7bb5"></span><span style="background:#3b5a9a"></span></div>
</section>

<footer class="footer">
  <h4 style="left:127px;top:16px;width:170px">Quick Links</h4>
  <ul class="links" style="left:127px"><li>Home</li><li>People</li><li>Services</li><li>Ethics</li></ul>
  <ul class="links" style="left:203px"><li>Publications</li><li>Testimonials</li><li>Contact</li></ul>
  <div class="vrule" style="left:308px"></div>
  <h4 style="left:320px;top:16px;width:411px">Contact Information</h4>
  <div class="office" style="left:323px"><b>Kabul Office</b>
    <div class="row"><svg width="12" height="16" viewBox="0 0 12 16"><path d="M6 0a6 6 0 0 1 6 6c0 4-6 10-6 10S0 10 0 6a6 6 0 0 1 6-6z" fill="#2ea3d8"/><circle cx="6" cy="6" r="2" fill="#333"/></svg><span>Level 3 Cedar House, Block C, Wazir Akbar Khan, Kabul</span></div>
    <div class="row"><svg width="12" height="12" viewBox="0 0 12 12"><path d="M2 0l3 3-1.5 2a8 8 0 0 0 3.5 3.5L9 7l3 3-2 2C5 12 0 7 0 2z" fill="#2ea3d8"/></svg><span>93-700-555-010</span></div>
    <div class="row"><svg width="14" height="10" viewBox="0 0 14 10"><rect width="14" height="10" fill="#2ea3d8"/><path d="M0 0l7 6 7-6" fill="none" stroke="#333" stroke-width="1.2"/></svg><span>info@hlp-legal.af</span></div>
  </div>
  <div class="office" style="left:528px"><b>Dubai Office</b>
    <div class="row"><svg width="12" height="16" viewBox="0 0 12 16"><path d="M6 0a6 6 0 0 1 6 6c0 4-6 10-6 10S0 10 0 6a6 6 0 0 1 6-6z" fill="#2ea3d8"/><circle cx="6" cy="6" r="2" fill="#333"/></svg><span>Level 9 Marina Court Tower 2, Harbour Road, Dubai, UAE</span></div>
    <div class="row"><svg width="12" height="12" viewBox="0 0 12 12"><path d="M2 0l3 3-1.5 2a8 8 0 0 0 3.5 3.5L9 7l3 3-2 2C5 12 0 7 0 2z" fill="#2ea3d8"/></svg><span>971 500 555 210</span></div>
    <div class="row"><svg width="14" height="10" viewBox="0 0 14 10"><rect width="14" height="10" fill="#2ea3d8"/><path d="M0 0l7 6 7-6" fill="none" stroke="#333" stroke-width="1.2"/></svg><span>info@hlp-legal.af</span></div>
  </div>
  <div class="vrule" style="left:745px"></div>
  <div class="copy"><div class="name">Hindukush Legal Partners</div>© Hindukush Legal Partners.<br>All Rights Reserved.</div>
</footer>
</body>
</html>
```